Tidewell show guide

I need to design a one page 7x10 pdf that will be printed. It will include our logo and the following text:

#1 Disaster Mitigation Lead Platform

We generated over 60 million in
revenue last year fo our contractors.

Leads types:
-Water Damage
-Fire Damage
-Mold Remediation
-Biohazard
-Plumbing
-Carpet Cleaning

Exclusive leads
No monthly fees
Only pay for valid leads

Stop by booth 814 to get to your cut!

Target Market(s)

Home service contractors

Colors
9bcb3b
0255a3

Requirements
Must have
• our logo and text
Should not have
• any clutter

```html
<!DOCTYPE html>
<html lang="en">
<head>
<meta charset="utf-8">
<title>Tidewell show guide</title>
<link rel="stylesheet" href="https://fonts.googleapis.com/css2?family=Fira+Sans:wght@600;700&display=swap">
<style>
  :root {
    --green: #10a04a;
    --blue: #4a78bf;
    --white: #ffffff;
    --ink: #111111;
    --shadow: rgba(0, 0, 0, 0.45);
  }
  * { margin: 0; padding: 0; box-sizing: border-box; }
  html, body { width: 840px; height: 1200px; overflow: hidden; }
  body {
    position: relative;
    background: var(--green);
    font-family: "Fira Sans", Arial, sans-serif;
  }
  .rank-badge {
    position: absolute;
    left: 214px; top: 22px;
    width: 382px; height: 382px;
    border-radius: 50%;
    background: var(--white);
    border: 28px solid var(--blue);
  }
  .rank-badge__number {
    position: absolute;
    left: 0; right: 0; top: 22px;
    text-align: center;
    font-size: 200px;
    font-weight: 700;
    line-height: 1;
    color: var(--blue);
    letter-spacing: -4px;
    text-shadow: 2px 3px 2px var(--shadow);
  }
  .headline {
    position: absolute;
    left: 118px; top: 273px;
    width: 586px; height: 165px;
  }
  .headline svg { position: absolute; inset: 0; }
  .headline__text {
    position: absolute;
    left: 0; right: 0; top: 14px;
    text-align: center;
    color: var(--white);
    font-weight: 700;
    font-size: 58px;
    line-height: 70px;
    text-shadow: 2px 3px 2px var(--shadow);
  }
  .headline__text span { display: block; }
  .revenue {
    position: absolute;
    left: 68px; top: 470px;
    width: 704px; height: 106px;
    background: var(--white);
    border-radius: 53px;
    padding: 0 0 0 40px;
    color: var(--green);
    font-weight: 700;
    font-size: 37px;
    letter-spacing: -0.3px;
    line-height: 46px;
    display: flex; flex-direction: column; justify-content: center;
  }
  .revenue__figure {
    color: var(--blue);
    font-size: 50px;
    text-decoration: underline;
    text-decoration-thickness: 3px;
    text-underline-offset: 4px;
  }
  .offer-panel {
    position: absolute;
    left: 42px; top: 592px;
    width: 756px; height: 640px;
    background: var(--white);
    border-radius: 48px;
  }
  .lead-types__title {
    position: absolute;
    left: 98px; top: 30px;
    width: 248px; height: 52px;
    background: var(--blue);
    color: var(--white);
    font-weight: 700;
    font-size: 35px;
    line-height: 52px;
    text-align: center;
    text-shadow: 1px 2px 2px var(--shadow);
  }
  .lead-types__list {
    position: absolute;
    left: 52px; top: 104px;
    list-style: none;
  }
  .lead-types__item {
    display: flex; align-items: center;
    height: 50px;
    font-size: 32px;
    font-weight: 700;
    color: var(--ink);
  }
  .lead-types__icon { width: 36px; height: 32px; margin-right: 18px; margin-top: 6px; }
  .perk {
    position: absolute;
    right: 44px;
    height: 44px;
    background: var(--green);
    color: var(--white);
    font-weight: 700;
    font-size: 29px;
    line-height: 44px;
    text-align: center;
    text-shadow: 1px 2px 2px var(--shadow);
  }
  .perk--exclusive { top: 112px; width: 248px; }
  .perk--fees { top: 205px; width: 251px; }
  .perk--valid { top: 293px; width: 349px; }
  .booth-call {
    position: absolute;
    left: 52px; top: 440px;
    width: 664px; height: 74px;
    background: var(--blue);
    border-radius: 37px;
    color: var(--white);
    font-weight: 700;
    font-size: 35px;
    line-height: 74px;
    text-align: center;
    text-shadow: 1px 2px 2px var(--shadow);
  }
  .brand {
    position: absolute;
    left: 0; right: 0; top: 542px;
    text-align: center;
    color: var(--blue);
    font-weight: 700;
    font-size: 30px;
    line-height: 48px;
  }
</style>
</head>
<body>
  <div class="rank-badge">
    <div class="rank-badge__number">#1</div>
  </div>

  <div class="headline">
    <svg width="586" height="165" viewBox="0 0 586 165" aria-hidden="true">
      <polygon points="0,0 586,0 586,165 54,165 54,107 0,107" fill="var(--blue)"/>
    </svg>
    <h1 class="headline__text"><span>Disaster Mitigation</span><span>Lead Platform</span></h1>
  </div>

  <p class="revenue">
    <span>We generated over <span class="revenue__figure">60</span> million in</span>
    <span>revenue last year for our contractors</span>
  </p>

  <section class="offer-panel">
    <h2 class="lead-types__title">LEADS TYPES</h2>
    <ul class="lead-types__list">
      <li class="lead-types__item"><svg class="lead-types__icon" viewBox="0 0 36 32" aria-hidden="true"><path d="M0 18 L7 14 L13 22 L35 1 L14 31 Z" fill="var(--blue)"/></svg>Water Damage</li>
      <li class="lead-types__item"><svg class="lead-types__icon" viewBox="0 0 36 32" aria-hidden="true"><path d="M0 18 L7 14 L13 22 L35 1 L14 31 Z" fill="var(--blue)"/></svg>Fire Damage</li>
      <li class="lead-types__item"><svg class="lead-types__icon" viewBox="0 0 36 32" aria-hidden="true"><path d="M0 18 L7 14 L13 22 L35 1 L14 31 Z" fill="var(--blue)"/></svg>Mold Remediation</li>
      <li class="lead-types__item"><svg class="lead-types__icon" viewBox="0 0 36 32" aria-hidden="true"><path d="M0 18 L7 14 L13 22 L35 1 L14 31 Z" fill="var(--blue)"/></svg>Biohazard</li>
      <li class="lead-types__item"><svg class="lead-types__icon" viewBox="0 0 36 32" aria-hidden="true"><path d="M0 18 L7 14 L13 22 L35 1 L14 31 Z" fill="var(--blue)"/></svg>Plumbing</li>
      <li class="lead-types__item"><svg class="lead-types__icon" viewBox="0 0 36 32" aria-hidden="true"><path d="M0 18 L7 14 L13 22 L35 1 L14 31 Z" fill="var(--blue)"/></svg>Carpet Cleaning</li>
    </ul>

    <p class="perk perk--exclusive">Exclusive leads</p>
    <p class="perk perk--fees">No monthly fees</p>
    <p class="perk perk--valid">Only pay for valid leads</p>

    <p class="booth-call">Stop by booth 814 to get to your cut!</p>

    <p class="brand">Harbor Reach</p>
  </section>
</body>
</html>
```